sydney wedding photography business needs a business card design

we need a business card design for a sydney based wedding photography and videography business. our business name is :golden hour photography and video. our target clients are 24-35 yrs female. our style is candid, organic, natural, dynamic. we are a team of young photographers and videographers, and help brides to create memories that they will cherish for the rest of their lives. the logo will be provided. we want an elegant design that reflects our style, and also want to give a great impression to our clients that we are one of the best studios in sydney and our brand means quality and premium service.

Target Market(s)

bride to be, 24-35 years old, living in sydney and surrunding areas

Industry/Entity Type

Wedding Photography

Contact Information for Business Card

address: 57 marrow lane, bexton nsw 2041
mobile: 0431872056
phone: (02) 9361 2748
info@goldenhourstudio.net.au
www.goldenhourstudio.net.au
facebook:goldenhourbridals
instagram:goldenhourbridals

Font styles to use
Serif
Sans Serif

Requirements
Nice to have
• maybe add my slogan"memories beyond eternity" if the layout looks good
Should not have
• no black color, not good idea for wedding biz card

```html
<!DOCTYPE html>
<html lang="en">
<head>
<meta charset="utf-8">
<title>Golden Hour Photography – Business Card</title>
<link rel="stylesheet" href="https://fonts.googleapis.com/css2?family=Cinzel:wght@500&family=Lora:wght@400&display=swap">
<style>
  :root {
    --backdrop: #e9e4da;
    --card: #f8f4ec;
    --card-edge: #e2d9c6;
    --gold: #b08317;
    --gold-soft: rgba(196, 150, 40, 0.30);
    --gold-fade: rgba(196, 150, 40, 0);
  }
  * { margin: 0; padding: 0; box-sizing: border-box; }
  html, body {
    width: 1200px;
    height: 741px;
    overflow: hidden;
    background: var(--backdrop);
  }
  .canvas {
    position: relative;
    width: 1200px;
    height: 741px;
  }
  .card {
    position: absolute;
    top: 229px;
    width: 494px;
    height: 282px;
    background: var(--card);
    border-left: 1px solid var(--card-edge);
    box-shadow: 0 6px 18px rgba(80, 60, 20, 0.22);
    color: var(--gold);
    text-align: center;
  }
  .card--front { left: 99px; }
  .card--back { left: 608px; }

  .corner-ornament {
    position: absolute;
    width: 112px;
    height: 110px;
  }
  .corner-ornament--tl { top: 18px; left: 18px;
    background: radial-gradient(circle 108px at 0 0, var(--gold-soft), var(--gold-fade)); }
  .corner-ornament--tr { top: 18px; right: 18px;
    background: radial-gradient(circle 108px at 100% 0, var(--gold-soft), var(--gold-fade)); }
  .corner-ornament--bl { bottom: 18px; left: 18px;
    background: radial-gradient(circle 108px at 0 100%, var(--gold-soft), var(--gold-fade)); }
  .corner-ornament--br { bottom: 18px; right: 18px;
    background: radial-gradient(circle 108px at 100% 100%, var(--gold-soft), var(--gold-fade)); }

  .brand {
    position: absolute;
    left: 0;
    right: 0;
    font-family: "Cinzel", serif;
    font-weight: 500;
    color: var(--gold);
  }
  .brand__name {
    top: 108px;
    font-size: 34px;
    letter-spacing: 0.04em;
    line-height: 1;
  }
  .brand__line {
    top: 158px;
    font-size: 14px;
    letter-spacing: 0.55em;
    padding-left: 0.55em;
    line-height: 1;
  }

  .person {
    position: absolute;
    top: 40px;
    left: 0;
    right: 0;
  }
  .person__name {
    display: inline-block;
    font-family: "Cinzel", serif;
    font-weight: 500;
    font-size: 21px;
    line-height: 1;
    padding-bottom: 4px;
    border-bottom: 1.5px solid var(--gold);
  }
  .person__role {
    font-family: "Lora", serif;
    font-size: 14px;
    margin-top: 3px;
  }
  .contact {
    position: absolute;
    top: 118px;
    left: 130px;
    right: 130px;
    list-style: none;
    font-family: "Lora", serif;
    font-size: 12.5px;
    line-height: 17px;
    white-space: nowrap;
  }
</style>
</head>
<body>
  <main class="canvas">
    <section class="card card--front" aria-label="Card front">
      <div class="corner-ornament corner-ornament--tl" role="img" aria-label="Gold flourish ornament, top left corner"></div>
      <div class="corner-ornament corner-ornament--tr" role="img" aria-label="Gold flourish ornament, top right corner"></div>
      <div class="corner-ornament corner-ornament--bl" role="img" aria-label="Gold flourish ornament, bottom left corner"></div>
      <div class="corner-ornament corner-ornament--br" role="img" aria-label="Gold flourish ornament, bottom right corner"></div>
      <p class="brand brand__name">Golden Hour</p>
      <p class="brand brand__line">PHOTOGRAPHY</p>
    </section>

    <section class="card card--back" aria-label="Card back">
      <div class="corner-ornament corner-ornament--tl" role="img" aria-label="Gold flourish ornament, top left corner"></div>
      <div class="corner-ornament corner-ornament--tr" role="img" aria-label="Gold flourish ornament, top right corner"></div>
      <div class="corner-ornament corner-ornament--bl" role="img" aria-label="Gold flourish ornament, bottom left corner"></div>
      <div class="corner-ornament corner-ornament--br" role="img" aria-label="Gold flourish ornament, bottom right corner"></div>
      <div class="person">
        <p class="person__name">Employee Name</p>
        <p class="person__role">Owner</p>
      </div>
      <ul class="contact">
        <li>M 0431 872 056</li>
        <li>P (02) 9361 2748</li>
        <li>info@goldenhourstudio.net.au</li>
        <li>www.goldenhourstudio.net.au</li>
        <li>57 Marrow Lane, Bexton NSW 2041</li>
        <li>@goldenhourbridals</li>
      </ul>
    </section>
  </main>
</body>
</html>
```